Advertising Material for Event

We are needing some advertising material done for an event. It can all be roughly the same except the two social media posts. We need:
- A banner
- A flyer
- 2 X social media posts

I have attached some examples of what we have done in the past. I have also attached a word document with the information.

Our colours are:
NAVY BLUE: Hex = #041E42 // RGB = 4 / 30 / 66 // CMYK = 100 / 90 / 13 / 68 // Pantone = 289 C
LIME GREEN: Hex = #97D700 // RGB = 151 / 215 / 0 // CMYK = 46 / 0 / 90 / 0 // Pantone = 375 C
WHITE

Our font are:
Avenir next regular, bold and demi bold
Freshman

Colors

Designer to choose colors to be used in the design.

Requirements
Must have
• Include photos provided. All info provided
Nice to have
• not cluttered

```html
<!DOCTYPE html>
<html lang="en">
<head>
<meta charset="utf-8">
<title>2022 Cheerleading Team Placements</title>
<link href="https://fonts.googleapis.com/css2?family=Graduate&family=Nunito+Sans:wght@400;600;700;800&family=Oswald:wght@500;600&display=swap" rel="stylesheet">
<style>
  :root{
    --navy:#041E42;
    --navy-deep:#06142b;
    --ink:#0b0f1a;
    --lime:#97D700;
    --green-top:#6fbf1e;
    --green-title:#3e9a22;
    --white:#ffffff;
    --silver:#dcdfe2;
    --silver-edge:#2b2f36;
    --page:#f1f1f1;
  }
  *{margin:0;padding:0;box-sizing:border-box;}
  html,body{width:1200px;height:2626px;overflow:hidden;background:var(--page);}
  body{font-family:"Nunito Sans",sans-serif;color:var(--white);position:relative;}

  .flyer{
    position:absolute;left:50px;top:542px;width:1100px;height:1542px;overflow:hidden;
    background:linear-gradient(180deg,var(--green-top) 0%,#4fa31c 16%,#2f8a22 30%,#1c5a3a 48%,#0c2f55 60%,var(--navy) 70%,var(--navy-deep) 100%);
    box-shadow:0 8px 30px rgba(0,0,0,.25);
  }
  .top-band{position:absolute;left:0;top:0;width:100%;height:310px;
    background:linear-gradient(180deg,#7cc826 0%,#63b21f 100%);}

  .photo{position:absolute;}
  .photo--jump{left:10px;top:90px;width:280px;height:100px;border-radius:40px;
    background:linear-gradient(90deg,#1b2a4a,#2c3d63,#1b2a4a);opacity:.85;}
  .photo--stunt-right{left:950px;top:60px;width:150px;height:835px;border-radius:70px 70px 10px 10px;
    background:linear-gradient(180deg,#d8c7ad 0%,#2b3550 35%,#1c2742 70%,#d9c0a4 100%);opacity:.8;}
  .photo--stunt-left{left:95px;top:400px;width:280px;height:493px;border-radius:80px 80px 10px 10px;
    background:linear-gradient(180deg,#d7c3a8 0%,#2a3754 40%,#1d2843 75%,#d6bea2 100%);opacity:.8;}
  .photo--stunt-center{left:445px;top:395px;width:240px;height:498px;border-radius:80px 80px 10px 10px;
    background:linear-gradient(180deg,#e2d3bd 0%,#e8ecef 40%,#233050 70%,#cdd2d8 100%);opacity:.8;}

  .title-year{position:absolute;left:0;width:100%;top:52px;text-align:center;
    font-family:"Graduate",serif;font-weight:400;font-size:160px;line-height:1;letter-spacing:2px;
    color:var(--green-title);-webkit-text-stroke:8px var(--navy);paint-order:stroke fill;}
  .title-main{position:absolute;left:0;width:100%;top:222px;text-align:center;
    font-family:"Graduate",serif;font-size:82px;line-height:1;letter-spacing:3px;
    color:var(--silver);-webkit-text-stroke:4px var(--silver-edge);paint-order:stroke fill;}
  .title-sub{position:absolute;left:0;width:100%;top:310px;text-align:center;
    font-weight:800;font-size:46px;letter-spacing:1px;color:var(--white);}

  .invite{position:absolute;left:0;top:890px;width:100%;height:90px;}
  .invite svg{position:absolute;left:0;top:0;}
  .invite__text{position:absolute;left:0;width:100%;top:14px;text-align:center;
    font-weight:700;font-size:24px;line-height:1.2;}

  .schedule{position:absolute;left:0;top:1015px;width:100%;height:100px;}
  .date{position:absolute;left:72px;top:2px;width:275px;height:86px;display:flex;
    background:var(--navy);border-radius:6px;overflow:hidden;}
  .date__day{width:26px;flex:none;background:var(--lime);color:var(--navy);writing-mode:vertical-rl;transform:rotate(180deg);
    font-weight:800;font-size:13px;text-align:center;letter-spacing:.5px;}
  .date__num{width:123px;flex:none;background:var(--white);color:var(--ink);text-align:center;}
  .date__num b{display:block;font-family:"Oswald",sans-serif;font-weight:600;font-size:58px;line-height:62px;}
  .date__num b sup{font-size:32px;vertical-align:top;line-height:46px;}
  .date__num span{display:block;font-weight:800;font-size:15px;margin-top:-4px;}
  .date__year{flex:1;color:var(--lime);font-family:"Oswald",sans-serif;font-weight:500;font-size:62px;line-height:86px;text-align:center;}
  .session{position:absolute;top:0;text-align:center;white-space:nowrap;}
  .session--junior{left:368px;width:330px;}
  .session--senior{left:718px;width:330px;}
  .session__age{font-weight:700;font-size:25px;color:var(--white);letter-spacing:1px;}
  .session__age em{font-style:normal;color:var(--lime);}
  .session__time{font-weight:800;font-size:46px;line-height:1.1;}
  .session-divider{position:absolute;left:707px;top:8px;width:2px;height:76px;background:var(--lime);}

  .details{position:absolute;left:0;top:1137px;width:100%;height:72px;background:rgba(6,10,20,.75);
    border-top:2px solid var(--lime);}
  .details__place{position:absolute;left:80px;top:12px;display:flex;gap:18px;align-items:center;
    font-weight:700;font-size:19px;line-height:1.15;white-space:nowrap;}
  .details__divider{position:absolute;left:440px;top:14px;width:2px;height:44px;background:var(--lime);}
  .details__cost{position:absolute;left:472px;top:4px;display:flex;align-items:baseline;gap:12px;font-weight:800;white-space:nowrap;}
  .details__cost small{font-size:21px;}
  .details__cost strong{font-size:52px;color:var(--lime);line-height:1.1;}
  .details__cost span{font-size:18px;font-weight:700;}

  .open-week{position:absolute;left:71px;top:1262px;width:960px;height:118px;border:1.5px solid #c9ccd2;text-align:center;}
  .open-week__tag{position:absolute;left:50%;top:-20px;transform:translateX(-50%);width:470px;height:38px;
    background:var(--lime);color:var(--navy);font-weight:800;font-size:19px;line-height:38px;
    clip-path:polygon(3% 0,100% 0,97% 100%,0 100%);}
  .open-week__q{margin-top:24px;color:var(--lime);font-size:21px;}
  .open-week__body{font-size:17.5px;line-height:1.3;padding:0 40px;}
  .open-week__body em{font-style:normal;color:var(--lime);}

  .contact{position:absolute;left:72px;top:1414px;width:980px;height:70px;display:flex;align-items:center;gap:22px;white-space:nowrap;}
  .brand{display:flex;align-items:center;gap:10px;flex:none;}
  .brand__dot{flex:none;width:14px;height:14px;border-radius:50%;background:var(--lime);}
  .brand__name{font-weight:800;font-size:22px;color:var(--lime);line-height:1;}
  .contact__item{display:flex;align-items:center;gap:10px;font-size:20px;}
  .contact__item--phone{font-weight:800;font-size:28px;}
</style>
</head>
<body>
<main class="flyer">
  <div class="top-band"></div>

  <div class="photo photo--jump" role="img" aria-label="Photo of a cheerleader mid toe-touch jump"></div>
  <div class="photo photo--stunt-right" role="img" aria-label="Photo of a cheer team holding a flyer high in a stunt"></div>
  <div class="photo photo--stunt-left" role="img" aria-label="Photo of young cheerleaders lifting a flyer in a stunt"></div>
  <div class="photo photo--stunt-center" role="img" aria-label="Photo of a child cheerleader standing on a teammate's shoulders"></div>

  <h1 class="title-year">2022</h1>
  <p class="title-main">CHEERLEADING</p>
  <p class="title-sub">TEAM PLACEMENTS</p>

  <section class="invite">
    <svg width="1100" height="90" viewBox="0 0 1100 90" aria-hidden="true">
      <polygon points="40,84 64,4 1060,4 1036,84" fill="#07090f"/>
      <polygon points="26,84 50,4 60,4 36,84" fill="var(--lime)"/>
      <polygon points="1050,84 1074,4 1064,4 1040,84" fill="var(--lime)"/>
      <line x1="64" y1="4" x2="1060" y2="4" stroke="var(--lime)" stroke-width="3"/>
      <line x1="40" y1="84" x2="1036" y2="84" stroke="var(--lime)" stroke-width="2"/>
    </svg>
    <p class="invite__text">Try out for a cheerleading team!<br>Everyone is welcome and will be placed on a team, regardless of skill level.</p>
  </section>

  <section class="schedule">
    <div class="date">
      <div class="date__day">SATURDAY</div>
      <div class="date__num"><b>11<sup>th</sup></b><span>DECEMBER</span></div>
      <div class="date__year">2021</div>
    </div>
    <div class="session session--junior">
      <p class="session__age"><em>11 YEARS</em> AND <em>UNDER</em></p>
      <p class="session__time">3:30 - 4:30pm</p>
    </div>
    <div class="session-divider"></div>
    <div class="session session--senior">
      <p class="session__age"><em>12 YEARS</em> AND <em>OVER</em></p>
      <p class="session__time">4:45 - 5:45pm</p>
    </div>
  </section>

  <section class="details">
    <div class="details__place">
      <svg width="22" height="28" viewBox="0 0 22 28" aria-hidden="true">
        <path d="M11 2a8 8 0 0 0-8 8c0 6 8 14 8 14s8-8 8-14a8 8 0 0 0-8-8z" fill="none" stroke="var(--lime)" stroke-width="2.4"/>
        <circle cx="11" cy="10" r="3" fill="var(--lime)"/>
        <ellipse cx="11" cy="26" rx="8" ry="1.6" fill="var(--lime)"/>
      </svg>
      <p>Apex Gymsports,<br>14-16 Marlow Place Kingsdale</p>
    </div>
    <div class="details__divider"></div>
    <div class="details__cost"><small>COST:</small><strong>$10</strong><span>and includes an Apex merchandise pack</span></div>
  </section>

  <section class="open-week">
    <div class="open-week__tag">SEMI-COMPETITIVE TEAMS ALSO AVAILABLE</div>
    <p class="open-week__q">Unsure what cheerleading is like?</p>
    <p class="open-week__body">Come along to our open week to try it out with our current Apex cheerleading teams. Classes are available from the <em>6th-10th of December.</em> Please contact us for more information! Bookings are required.</p>
  </section>

  <footer class="contact">
    <div class="brand"><span class="brand__dot"></span><span class="brand__name">APEX<br>GYMSPORTS</span></div>
    <div class="contact__item contact__item--phone">
      <svg width="26" height="26" viewBox="0 0 24 24" aria-hidden="true"><path d="M6.6 10.8a15 15 0 0 0 6.6 6.6l2.2-2.2a1 1 0 0 1 1-.25 11.4 11.4 0 0 0 3.6.57 1 1 0 0 1 1 1V20a1 1 0 0 1-1 1A17 17 0 0 1 3 4a1 1 0 0 1 1-1h3.5a1 1 0 0 1 1 1c0 1.25.2 2.45.57 3.57a1 1 0 0 1-.25 1z" fill="var(--lime)"/></svg>
      95550172
    </div>
    <div class="contact__item">
      <svg width="24" height="18" viewBox="0 0 24 18" aria-hidden="true"><rect x="1" y="1" width="22" height="16" fill="none" stroke="var(--lime)" stroke-width="2"/><path d="M1 1l11 9 11-9" fill="none" stroke="var(--lime)" stroke-width="2"/></svg>
      cheer@apexgymsports.com
    </div>
    <div class="contact__item">
      <svg width="22" height="22" viewBox="0 0 22 22" aria-hidden="true"><circle cx="11" cy="11" r="9.5" fill="none" stroke="var(--lime)" stroke-width="2"/><ellipse cx="11" cy="11" rx="4" ry="9.5" fill="none" stroke="var(--lime)" stroke-width="1.6"/><line x1="1.5" y1="11" x2="20.5" y2="11" stroke="var(--lime)" stroke-width="1.6"/></svg>
      www.apexgymsports.com
    </div>
  </footer>
</main>
</body>
</html>
```